Photography blog homepage design

I need a new webpage design for my photography blog. My blog focuses on post-processing techniques, particularly in luminosity masking, HDR photography and other advanced photo editing skills. I want the new homepage to let visitors know instantly what the blog is about as this is currently not very obvious from the feedback I received. Apart from that, the homepage should also inform/showcase latest blog post and/or popular blog post and/or some of the training courses I offer (that's my idea, but I leave it to your expertise). There should also ideally have a CTA that leads visitors to the "Start Here" page where they can learn more about my blog. The bulk of my audience is intermediate/advanced photographers who are above 30-35 years old, with a significant group in the 60 to >75 age group. The design should convey trust and creativity at the same time. The color theme for my blog is orange and dark grey. URL is www.lumivarnic.com, you can use the current content on that page.

Target Market(s)

Intermediate/advanced photographers (hobbyist or professional) age 35-75 years old.

Number of Pages Required

1 page

Font styles to use
Sans Serif

Colors
faa54b
f68e4e
f78f20

Requirements
Must have
• Upside down homepage (menus at the bottom)

```html
<!DOCTYPE html>
<html lang="en">
<head>
<meta charset="utf-8">
<title>Lumivarnic — Photography Blog</title>
<link href="https://fonts.googleapis.com/css2?family=Lato:wght@400;700;900&display=swap" rel="stylesheet">
<style>
:root{
  --orange:#f78f20;
  --orange-soft:#faa54b;
  --orange-tag:#f68e4e;
  --dark:#222222;
  --ink:#2b2b2b;
  --muted:#8a8a8a;
  --line:#e6e6e6;
  --white:#ffffff;
}
*{box-sizing:border-box;margin:0;padding:0}
html,body{width:1200px;height:3210px;overflow:hidden;background:var(--white)}
body{position:relative;font-family:"Lato",sans-serif;color:var(--ink)}
.abs{position:absolute}
.photo{position:absolute;display:block}
.brand{display:flex;align-items:center;gap:10px;font-family:"Lato",sans-serif;font-weight:900;letter-spacing:-1px;text-transform:uppercase;line-height:1}
.brand .dot{width:.8em;height:.8em;border-radius:50%;background:var(--orange)}
.circle-btn{width:44px;height:44px;border-radius:50%;background:var(--orange);display:inline-block}

/* header */
.site-header .brand{left:90px;top:36px;font-size:50px;color:#111}
.search{left:685px;top:37px;width:253px;height:43px;border:1px solid #ccc;border-radius:22px;padding-left:16px;font-size:14px;color:#999;display:flex;align-items:center}
.search span{position:absolute;right:4px;top:4px;width:34px;height:34px;border-radius:50%;background:var(--orange-soft)}
.header-social{left:968px;top:36px;display:flex;gap:5px}

/* hero */
.hero{left:0;top:118px;width:1200px;height:403px;background:linear-gradient(180deg,#1b2230 0%,#2c3b55 38%,#0e1420 55%,#25324a 70%,#06080c 100%)}
.hero-copy{left:644px;top:214px;width:470px;color:var(--white)}
.hero-copy .brand{font-size:56px;color:var(--white)}
.hero-copy p{margin-top:16px;font-size:16px;line-height:33px}
.cta{left:649px;top:360px;width:202px;height:46px;background:var(--orange);color:var(--white);font-weight:700;font-size:18px;display:flex;align-items:center;justify-content:center}
.profile-fade{left:400px;top:521px;width:800px;height:120px;background:linear-gradient(180deg,#ececec,#fff 70%)}
.avatar{left:89px;top:361px;width:320px;height:320px;border-radius:50%;background:#fff;box-shadow:0 2px 10px rgba(0,0,0,.15)}
.avatar .photo{left:14px;top:14px;width:292px;height:292px;border-radius:50%;background:radial-gradient(circle at 50% 45%,#bdbdbd,#6f6f6f 60%,#3c3c3c)}
.author-name{left:412px;top:570px;font-size:38px;font-weight:700;color:var(--orange)}
.author-role{left:412px;top:619px;font-size:22px;font-weight:700}

/* posts */
.post{left:71px;width:684px;height:820px;border:1px solid var(--line);box-shadow:0 0 6px rgba(0,0,0,.06)}
.post .photo{left:7px;top:7px;width:670px;height:450px}
.post-title{position:absolute;left:7px;top:480px;font-size:21px;font-weight:700}
.post-meta{position:absolute;left:7px;top:520px;font-size:13px;font-weight:700;display:flex;align-items:center;gap:7px}
.post-meta i{width:9px;height:9px;border-radius:50%;background:var(--ink)}
.tags{position:absolute;left:7px;top:550px;display:flex;gap:8px}
.tag{background:var(--orange-tag);color:var(--white);font-size:13px;width:95px;height:26px;display:flex;align-items:center;justify-content:center}
.post-text{position:absolute;left:7px;top:584px;width:656px;font-size:15.5px;line-height:31px;color:var(--muted);text-align:justify}
.post-text b{color:var(--ink);font-weight:700;font-size:14px}
.post-foot{position:absolute;left:0;top:764px;width:682px;border-top:1px solid var(--line);height:55px;display:flex;align-items:center;padding:0 16px;font-size:15px;gap:18px}
.stat{display:flex;align-items:center;gap:5px}
.share{margin-left:auto;display:flex;gap:13px}
.share span{width:32px;height:32px;border-radius:50%;border:1px solid #ddd;position:relative}
.share span::after{content:"";position:absolute;left:12px;top:12px;width:7px;height:7px;border-radius:50%;background:var(--orange)}

/* sidebar */
.widget{left:779px;width:350px;border:1px solid var(--line);box-shadow:0 0 6px rgba(0,0,0,.06)}
.widget-head{height:46px;background:var(--orange);color:var(--white);font-size:20px;font-weight:400;display:flex;align-items:center;justify-content:center;letter-spacing:.3px}
.about .photo{left:30px;top:73px;width:291px;height:290px;background:linear-gradient(180deg,#b9b3aa,#8f887e 45%,#e0a079 70%,#d9d4cc)}
.about .brand{position:absolute;left:22px;top:382px;font-size:38px;color:#111}
.about p{position:absolute;left:30px;top:432px;width:291px;font-size:13.5px;line-height:30px;text-align:justify;text-align-last:center}
.about .more{position:absolute;left:0;width:348px;top:622px;text-align:center;color:var(--orange);font-size:16px}
.pop-item,.news-item{position:absolute;left:27px;display:flex;gap:16px}
.pop-item .thumb{width:91px;height:75px;position:relative}
.pop-item h4,.news-item h4{color:var(--orange);font-size:14px;font-weight:400;margin-top:8px}
.pop-item p{font-size:12px;line-height:24px;margin-top:4px;width:200px}
.news-item .thumb{width:91px;height:74px;position:relative}
.news-item h4{margin-top:18px;font-size:15px}
.news-item small{display:block;font-size:12px;color:var(--muted);margin-top:8px}
.cat-list{list-style:none;padding:0 10px}
.cat-list li{height:47.5px;border-bottom:1px solid var(--line);display:flex;align-items:center;font-size:18px;text-transform:uppercase;padding-left:1px}
.cat-list li:last-child{border:0}

/* training */
.section-title{left:71px;top:2448px;font-size:34px;font-weight:700;color:var(--orange)}
.course-lead .photo{left:76px;top:2506px;width:518px;height:264px;background:linear-gradient(180deg,#2a2a30,#6c5a5e 50%,#2d2a2c)}
.course-lead h3{position:absolute;left:71px;top:2791px;font-size:24px;font-weight:400;color:var(--orange)}
.course-lead p{position:absolute;left:76px;top:2836px;width:518px;font-size:16.5px;line-height:32px;text-align:justify}
.course{width:255px}
.course .photo{position:relative;width:255px;height:152px}
.course h4{margin-top:18px;font-size:16px;font-weight:400;color:var(--orange)}
.course p{font-size:11.5px;line-height:24px;text-align:justify;margin-top:2px}

/* footer */
.site-footer{left:0;top:3025px;width:1200px;height:185px;background:var(--dark);color:var(--white);text-align:center}
.foot-social{position:absolute;left:521px;top:29px;display:flex;gap:14px}
.foot-nav{position:absolute;top:96px;width:100%;font-size:16px;word-spacing:2px}
.copyright{position:absolute;top:138px;width:100%;font-size:14px;font-weight:700;letter-spacing:.5px}
</style>
</head>
<body>

<header class="site-header">
  <div class="abs brand">Lumivarnic<span class="dot"></span></div>
  <div class="abs search">Search<span></span></div>
  <div class="abs header-social" aria-label="Social links">
    <span class="circle-btn"></span><span class="circle-btn"></span><span class="circle-btn"></span>
  </div>
</header>

<section>
  <div class="abs hero" role="img" aria-label="City skyline at night reflected in still water"></div>
  <div class="abs hero-copy">
    <div class="brand">Lumivarnic<span class="dot"></span></div>
    <p>Sed ut perspiciatis unde omnis iste natus error accusantium doloremque aperiam.</p>
  </div>
  <a class="abs cta">START HERE &#10140;</a>
  <div class="abs profile-fade"></div>
  <div class="abs avatar"><div class="photo" role="img" aria-label="Black and white portrait of the author"></div></div>
  <div class="abs author-name">TAVREN</div>
  <div class="abs author-role">Author of Lumivarnic</div>
</section>

<article class="abs post" style="top:721px">
  <div class="photo" role="img" aria-label="Domed classical pavilion reflected in a lake under a cloudy sky" style="background:linear-gradient(180deg,#5a7ea0,#9fb6c6 35%,#7a5e4c 50%,#8a9aa8 75%,#2f3a40)"></div>
  <h2 class="post-title">Lorem ipsum dolor sit amet, consectetur adipiscing</h2>
  <div class="post-meta">MARCH 13, 2019 <i></i> NO COMMENTS</div>
  <div class="tags"><span class="tag">Photograpy</span><span class="tag">Editing</span></div>
  <p class="post-text">Sed ut perspiciatis unde omnis iste natus error sit voluptatem accusantium doloremque laudantium, totam rem aperiam, eaque ipsa quae ab illo inventore veritatis et quasi architecto beatae vitae dicta sunt explicabo. Nemo enim ipsam voluptatem quia voluptas sit aspernatur aut odit aut fugit, sed quia consequuntur magni dolores eos qui ratione voluptatem sequi nesciunt... &nbsp;<b>CONTINUE READING</b></p>
  <div class="post-foot">
    <span class="stat">&#9650; 8</span><span class="stat">&#9679; 8</span><span class="stat">&#8630; Reply</span>
    <span class="share"><span></span><span></span><span></span><span></span></span>
  </div>
</article>

<article class="abs post" style="top:1584px">
  <div class="photo" role="img" aria-label="Aerial view of waves washing onto a sandy beach" style="background:linear-gradient(160deg,#c9b096 0%,#b59e88 35%,#2f4a5e 55%,#4d6a7e 80%,#8a857c)"></div>
  <h2 class="post-title">Lorem ipsum dolor sit amet, consectetur adipiscing</h2>
  <div class="post-meta">MARCH 13, 2019 <i></i> NO COMMENTS</div>
  <div class="tags"><span class="tag">Photograpy</span><span class="tag">Editing</span></div>
  <p class="post-text">Sed ut perspiciatis unde omnis iste natus error sit voluptatem accusantium doloremque laudantium, totam rem aperiam, eaque ipsa quae ab illo inventore veritatis et quasi architecto beatae vitae dicta sunt explicabo. Nemo enim ipsam voluptatem quia voluptas sit aspernatur aut odit aut fugit, sed quia consequuntur magni dolores eos qui ratione voluptatem sequi nesciunt... &nbsp;<b>CONTINUE READING</b></p>
  <div class="post-foot">
    <span class="stat">&#9650; 8</span><span class="stat">&#9679; 8</span><span class="stat">&#8630; Reply</span>
    <span class="share"><span></span><span></span><span></span><span></span></span>
  </div>
</article>

<aside>
  <section class="abs widget about" style="top:721px;height:656px">
    <div class="widget-head">ABOUT</div>
    <div class="photo" role="img" aria-label="Author standing in front of stone columns"></div>
    <div class="brand">Lumivarnic<span class="dot"></span></div>
    <p>Sed ut perspiciatis unde omnis iste natus error sit voluptatem accusantium doloremque laudantium, totam rem aperiam, eaque ipsa quae ab illo inventore veritatis et quasi architecto sunt explicabo. ratione voluptatem sequi nesciunt.</p>
    <div class="more">VIEW MORE</div>
  </section>

  <section class="abs widget" style="top:1387px;height:415px">
    <div class="widget-head">MOST POPULAR</div>
    <div class="pop-item" style="top:80px"><div class="thumb photo" role="img" aria-label="Dark landscape roundup cover" style="background:linear-gradient(180deg,#3a4654,#0f1418)"></div><div><h4>LOREM IPSUM</h4><p>Sed ut perspiciatis unde omnis iste natus error sit voluptatem</p></div></div>
    <div class="pop-item" style="top:196px"><div class="thumb photo" role="img" aria-label="Mountain valley at sunset" style="background:linear-gradient(180deg,#c9a46e,#5e6a4a 55%,#3a3a30)"></div><div><h4>LOREM IPSUM</h4><p>Sed ut perspiciatis unde omnis iste natus error sit voluptatem</p></div></div>
    <div class="pop-item" style="top:304px"><div class="thumb photo" role="img" aria-label="Highland cattle in a field" style="background:linear-gradient(180deg,#8fa6c4,#7a5238 55%,#4a4030)"></div><div><h4>LOREM IPSUM</h4><p>Sed ut perspiciatis unde omnis iste natus error sit voluptatem</p></div></div>
  </section>

  <section class="abs widget" style="top:1813px;height:288px">
    <div class="widget-head">LATEST &nbsp;NEWS</div>
    <div class="news-item" style="top:85px;left:24px"><div class="thumb photo" role="img" aria-label="Black and white skyscraper from below" style="background:linear-gradient(135deg,#ddd,#444 60%,#111)"></div><div><h4>LOREM IPSUM DOLOR</h4><small>APRIL 26, 2019</small></div></div>
    <div class="news-item" style="top:193px;left:24px"><div class="thumb photo" role="img" aria-label="Person standing in a stone archway" style="background:linear-gradient(180deg,#b69a7a,#5a4634)"></div><div><h4>LOREM IPSUM DOLOR</h4><small>APRIL 26, 2019</small></div></div>
  </section>

  <section class="abs widget" style="top:2112px;height:289px">
    <div class="widget-head">CATEGORIES</div>
    <ul class="cat-list">
      <li>Blog</li><li>Tutorial</li><li>Latest Blogs</li><li>Popular Blogs</li><li>Training Courses</li>
    </ul>
  </section>
</aside>

<section>
  <h2 class="abs section-title">TRAINING COURSES</h2>
  <div class="course-lead">
    <div class="photo" role="img" aria-label="City street between tall buildings leading to a bridge tower at dusk"></div>
    <h3>SED UT PERSPICIATIS UNDE OMNIS</h3>
    <p>At vero eos et accusamus et iusto odio dignissimos ducimus qui blanditiis praesentium voluptatum deleniti atque corrupti quos dolores et quas molestias excepturi sint occaecati cupiditate non provident, similique sunt in culpa qui officia deserunt mollitia animi, id est laborum et dolorum fuga.</p>
  </div>
  <div class="abs course" style="left:613px;top:2506px"><div class="photo" role="img" aria-label="Church beside a lake with grassy banks" style="background:linear-gradient(180deg,#9ab0c8,#7b7a4c 55%,#2f3b44)"></div><h4>SED UT PERSPICIATIS</h4><p>But I must explain to you how all this mistaken idea of denouncing</p></div>
  <div class="abs course" style="left:878px;top:2506px"><div class="photo" role="img" aria-label="Clock tower at blue hour framed by trees" style="background:linear-gradient(180deg,#4b5c9a,#6b5a8a 50%,#24302a)"></div><h4>SED UT PERSPICIATIS</h4><p>But I must explain to you how all this mistaken idea of denouncing</p></div>
  <div class="abs course" style="left:613px;top:2762px"><div class="photo" role="img" aria-label="Waterfall with sunlight breaking through mist" style="background:linear-gradient(180deg,#d9a866,#b7a78e 45%,#4a4a48)"></div><h4>SED UT PERSPICIATIS</h4><p>But I must explain to you how all this mistaken idea of denouncing</p></div>
  <div class="abs course" style="left:878px;top:2762px"><div class="photo" role="img" aria-label="City skyline at dusk reflected in water" style="background:linear-gradient(180deg,#4a5a9c,#7a4a78 50%,#1e2440)"></div><h4>SED UT PERSPICIATIS</h4><p>But I must explain to you how all this mistaken idea of denouncing</p></div>
</section>

<footer class="abs site-footer">
  <div class="foot-social" aria-label="Social links"><span class="circle-btn"></span><span class="circle-btn"></span><span class="circle-btn"></span></div>
  <nav class="foot-nav">Home &nbsp;| &nbsp;About Me &nbsp;| &nbsp;Blog &nbsp;| &nbsp;Tutorials &nbsp;| &nbsp;Contact</nav>
  <div class="copyright">Copyright © 2019. All Rights Reserved. Privacy Policy | Terms &amp; Conditions</div>
</footer>

</body>
</html>
```